Headlight Restoration kit

This work is for a Bidzo description listing in HTML for a DIY Headlight Restoration Kit, Please view photos,

I have an existing Bidzo listing that needs to be updated as its very old and not professional touch, i would like a completely new design and layout.

It will need to contain images of the product and full description. I have some screen shots of the old listing to help. It will need to be in HTML Format.

```html
<!DOCTYPE html>
<html lang="en">
<head>
<meta charset="utf-8">
<title>DIY Heavy Duty Headlight Restoration Kit</title>
<link href="https://fonts.googleapis.com/css2?family=Cantarell:wght@400;700&display=swap" rel="stylesheet">
<style>
  :root {
    --brand-green: #2dec9a;
    --page-bg: #f8f8f8;
    --ink: #212529;
  }
  * { box-sizing: border-box; margin: 0; padding: 0; }
  html, body {
    width: 1200px;
    height: 307px;
    overflow: hidden;
    background: var(--page-bg);
    font-family: "Cantarell", Arial, sans-serif;
    color: var(--ink);
  }
  .listing { width: 1200px; height: 307px; position: relative; }
  .hero {
    height: 129px;
    background: var(--brand-green);
    text-align: center;
    position: relative;
  }
  .hero-title {
    position: absolute;
    top: 7px; left: 0; right: 0;
    font-size: 28px;
    font-weight: 700;
    line-height: 36px;
  }
  .hero-note {
    position: absolute;
    top: 58px; left: 0; right: 0;
    font-size: 14px;
    line-height: 20px;
  }
  .hero-rule {
    position: absolute;
    top: 102px;
    left: 555px;
    width: 93px;
    height: 2px;
    background: var(--ink);
  }
  .features {
    display: flex;
    gap: 28px;
    padding-left: 86px;
    padding-top: 22px;
  }
  .feature { width: 325px; }
  .feature-icon {
    display: block;
    width: 30px;
    height: 30px;
    margin: 0 auto;
    fill: var(--ink);
  }
  .feature-title {
    text-align: center;
    font-size: 15px;
    font-weight: 700;
    line-height: 20px;
    margin-top: 11px;
  }
  .feature-text {
    font-size: 14px;
    line-height: 21.5px;
    text-align: justify;
    margin-top: 7px;
  }
</style>
</head>
<body>
<main class="listing">
  <header class="hero">
    <h1 class="hero-title">DIY Heavy Duty Headlight Restoration kit</h1>
    <p class="hero-note">(Please follow instruction carefully)</p>
    <div class="hero-rule"></div>
  </header>

  <section class="features">
    <article class="feature">
      <svg class="feature-icon" viewBox="0 0 32 32" aria-hidden="true">
        <circle cx="16" cy="16" r="15"/>
        <path d="M12 8h6a5 5 0 0 1 0 10h-3v6h-3z M15 11v4h3a2 2 0 0 0 0-4z" fill="#f8f8f8" fill-rule="evenodd"/>
      </svg>
      <h2 class="feature-title">Product</h2>
      <p class="feature-text">Lorem ipsum dolor sit amet, consectetur adipiscing elit, sed do eiusmod tempor incididunt ut labore et dolore magna aliqua.</p>
    </article>

    <article class="feature">
      <svg class="feature-icon" viewBox="0 0 36 32" aria-hidden="true" style="width:40px">
        <path d="M1 2h5v20h29v3H3V5H1z"/>
        <rect x="9" y="4" width="12" height="16" rx="1"/>
        <rect x="22" y="4" width="12" height="16" rx="1"/>
        <rect x="13" y="4" width="4" height="5" fill="#f8f8f8"/>
        <rect x="26" y="4" width="4" height="5" fill="#f8f8f8"/>
        <circle cx="8" cy="28" r="3"/>
        <circle cx="30" cy="28" r="3"/>
      </svg>
      <h2 class="feature-title">Shipping</h2>
      <p class="feature-text">Lorem ipsum dolor sit amet, consectetur adipiscing elit, sed do eiusmod tempor incididunt ut labore et dolore magna aliqua.</p>
    </article>

    <article class="feature">
      <svg class="feature-icon" viewBox="0 0 36 32" aria-hidden="true" style="width:38px">
        <rect x="1" y="4" width="34" height="25" rx="2"/>
        <circle cx="11" cy="13" r="3.5" fill="#f8f8f8"/>
        <path d="M5 23c0-4 3-6 6-6s6 2 6 6z" fill="#f8f8f8"/>
        <rect x="20" y="11" width="11" height="2" fill="#f8f8f8"/>
        <rect x="20" y="15" width="11" height="2" fill="#f8f8f8"/>
        <rect x="20" y="19" width="11" height="2" fill="#f8f8f8"/>
      </svg>
      <h2 class="feature-title">Contact</h2>
      <p class="feature-text">Lorem ipsum dolor sit amet, consectetur adipiscing elit, sed do eiusmod tempor incididunt ut labore et dolore magna aliqua.</p>
    </article>
  </section>
</main>
</body>
</html>
```